Corvane Holdings needs a business card

I would like the card to be simple but modern and elegant.
I like black and white.
or black and gold.
we are a private finance lender and also are involved in property and property developments.

please look at the business card photos i provided i would like C.H only one one side and all the other details on the other side use fonts that tie in with my theme.

Industry/Entity Type

Finance

Contact Information for Business Card

Corvane Holdings (C.H) Elliot Marbury M: 0413586102 E: elliotmar@examplemail.net

Font styles to use
Other font styles liked:
• Use fonts that would reflect our business

Colors
000000
ffffff

Requirements
Must have
• one side of details
• other side has either C.H or Corvane Holdings like in the photos provided

```html
<!DOCTYPE html>
<html lang="en">
<head>
<meta charset="utf-8">
<title>Corvane Holdings — Business Card</title>
<link href="https://fonts.googleapis.com/css2?family=Exo+2:wght@500;600&family=Open+Sans:wght@400&display=swap" rel="stylesheet">
<style>
  :root {
    --backdrop: #2b2b2b;
    --card: #000000;
    --ink: #ffffff;
    --rule: #d9d9d9;
  }
  html, body {
    margin: 0;
    padding: 0;
    width: 1200px;
    height: 900px;
    overflow: hidden;
    background: var(--backdrop);
  }
  .canvas {
    width: 1200px;
    height: 900px;
    display: flex;
    flex-direction: column;
    align-items: center;
    justify-content: center;
    gap: 40px;
  }
  .card {
    position: relative;
    width: 700px;
    height: 400px;
    background: var(--card);
    box-shadow: 0 10px 30px rgba(0,0,0,0.45);
    overflow: hidden;
  }

  /* Front: monogram on a rule */
  .front .monogram-rule {
    position: absolute;
    left: 0;
    right: 0;
    top: 300px;
    display: flex;
    align-items: center;
  }
  .front .rule-segment {
    flex: 1;
    height: 1px;
    background: var(--rule);
  }
  .front .monogram {
    font-family: "Exo 2", sans-serif;
    font-weight: 600;
    font-size: 54px;
    letter-spacing: 2px;
    color: var(--ink);
    padding: 0 26px;
    line-height: 1;
  }

  /* Back: contact details */
  .back .contact {
    position: absolute;
    right: 40px;
    top: 168px;
    text-align: right;
    font-family: "Open Sans", sans-serif;
    font-size: 15px;
    letter-spacing: 1.2px;
    line-height: 1.55;
    color: var(--ink);
  }
  .back .contact .label {
    margin-right: 8px;
  }
  .back .edge-mark {
    position: absolute;
    left: 0;
    top: 336px;
    width: 4px;
    height: 30px;
    background: var(--ink);
  }
  .back .holder {
    position: absolute;
    left: 40px;
    top: 300px;
  }
  .back .holder-name {
    font-family: "Exo 2", sans-serif;
    font-weight: 500;
    font-size: 22px;
    letter-spacing: 0.5px;
    text-transform: uppercase;
    color: var(--ink);
    margin: 0;
    padding-bottom: 8px;
    padding-right: 14px;
    border-bottom: 1px solid var(--rule);
    display: inline-block;
  }
</style>
</head>
<body>
  <main class="canvas">
    <section class="card front" aria-label="Card front">
      <div class="monogram-rule">
        <span class="rule-segment"></span>
        <span class="monogram">C.H</span>
        <span class="rule-segment"></span>
      </div>
    </section>

    <section class="card back" aria-label="Card back">
      <div class="contact">
        <div><span class="label">M:</span>041.358.6102</div>
        <div><span class="label">E:</span>elliotmar@examplemail.net</div>
      </div>
      <span class="edge-mark"></span>
      <div class="holder">
        <h1 class="holder-name">Elliot Marbury</h1>
      </div>
    </section>
  </main>
</body>
</html>
```